Kestrel Gardenworks Business Card

An eye catching, yet simple business card that includes;

1. our logo
2. office phone - 5083172946
3. email - kestrelgardenworks@mailbrook.com
4. website - www.kestrelgardenworks.com
5. instagram - @kestrelgardenworksnv

```html
<!DOCTYPE html>
<html lang="en">
<head>
<meta charset="utf-8">
<title>Kestrel Gardenworks Business Card</title>
<link rel="stylesheet" href="https://fonts.googleapis.com/css2?family=Open+Sans:wght@400;600;700&display=swap">
<style>
  :root {
    --backdrop: #d8d2cb;
    --card-light: #ece8e2;
    --card-dark: #2a2522;
    --copper: #a45a23;
    --copper-soft: #c07a3e;
    --ink-light: #e6ddd3;
    --logo-ink: #2e2825;
  }
  * { margin: 0; padding: 0; box-sizing: border-box; }
  html, body {
    width: 1200px;
    height: 1047px;
    overflow: hidden;
    background: var(--backdrop);
    font-family: "Open Sans", Arial, sans-serif;
  }
  .card {
    position: absolute;
    left: 100px;
    top: 250px;
    width: 1000px;
    height: 546px;
    border-radius: 26px;
    overflow: hidden;
    background: var(--card-light);
    box-shadow: 0 10px 30px rgba(0,0,0,0.15);
  }
  .card-shape { position: absolute; inset: 0; }
  .brand {
    position: absolute;
    left: 60px;
    top: 100px;
    display: flex;
    align-items: center;
    gap: 16px;
  }
  .brand-dot {
    width: 26px;
    height: 26px;
    border-radius: 50%;
    background: var(--copper);
  }
  .brand-name {
    font-size: 42px;
    font-weight: 700;
    color: var(--logo-ink);
    letter-spacing: 0.5px;
  }
  .holder {
    position: absolute;
    right: 44px;
    top: 230px;
    text-align: right;
  }
  .holder-name {
    font-size: 34px;
    font-weight: 600;
    color: var(--copper-soft);
    line-height: 1.1;
    letter-spacing: 0.5px;
  }
  .holder-role {
    font-size: 24px;
    color: var(--ink-light);
    margin-top: 6px;
  }
  .holder-bar {
    position: absolute;
    right: 0;
    top: 236px;
    width: 24px;
    height: 66px;
    background: var(--copper);
  }
  .contacts {
    position: absolute;
    right: 16px;
    top: 372px;
    list-style: none;
  }
  .contact {
    display: flex;
    justify-content: flex-end;
    align-items: center;
    gap: 10px;
    height: 35px;
    font-size: 23px;
    color: var(--ink-light);
  }
  .contact-icon { width: 22px; height: 22px; flex: none; }
</style>
</head>
<body>
  <div class="card">
    <svg class="card-shape" viewBox="0 0 1000 546" width="1000" height="546">
      <path d="M683,0 C770,90 720,210 610,330 C500,450 405,490 385,546 L1000,546 L1000,0 Z" fill="var(--card-dark)"/>
      <path d="M660,28 C720,110 680,215 575,330 C480,435 418,480 398,536" fill="none" stroke="var(--copper)" stroke-width="7" stroke-linecap="round"/>
    </svg>

    <div class="brand">
      <span class="brand-dot"></span>
      <span class="brand-name">Kestrel Gardenworks</span>
    </div>

    <div class="holder">
      <p class="holder-name">DANIEL HARTLEY</p>
      <p class="holder-role">Managing Director</p>
    </div>
    <span class="holder-bar"></span>

    <ul class="contacts">
      <li class="contact">5083172946
        <svg class="contact-icon" viewBox="0 0 24 24"><path d="M3 9c2-4 16-4 18 0l-3 2-2-2v-1H8v1l-2 2zM6 12h12l2 7H4z" fill="var(--copper-soft)"/></svg>
      </li>
      <li class="contact">kestrelgardenworks@mailbrook.com
        <svg class="contact-icon" viewBox="0 0 24 24"><rect x="3" y="6" width="18" height="13" rx="1" fill="none" stroke="var(--copper-soft)" stroke-width="2"/><path d="M3 7l9 7 9-7" fill="none" stroke="var(--copper-soft)" stroke-width="2"/></svg>
      </li>
      <li class="contact">www.kestrelgardenworks.com
        <svg class="contact-icon" viewBox="0 0 24 24"><circle cx="12" cy="12" r="9" fill="none" stroke="var(--copper-soft)" stroke-width="2"/><path d="M3 12h18M12 3c-4 5-4 13 0 18M12 3c4 5 4 13 0 18" fill="none" stroke="var(--copper-soft)" stroke-width="1.5"/></svg>
      </li>
      <li class="contact">@kestrelgardenworksnv
        <svg class="contact-icon" viewBox="0 0 24 24"><rect x="4" y="4" width="16" height="16" rx="2" fill="none" stroke="var(--copper-soft)" stroke-width="2"/></svg>
      </li>
    </ul>
  </div>
</body>
</html>
```